Exciting Real Estate Project Needs A Flyer Design

We need a flyer designed for a real estate development in Australia called Bolderan Yards Tuggerah. We develop outstanding functional industrial warehouse spaces for a wide range of industries and personal uses. We are going to use the flyer to mail out to local businesses to see if we can solve their storage / lack of space issues by them buying a unit from us. Note the units are not built yet they are selling off the plan. More details, branding colours can be found at www.bolderanyardstuggerah.com.au. The final design should communicate confidence, using executive colours, and contrasting the problem of lack of storage and mess with the productivity increases and being a better business once they own one of the units. I have attached a briefing document for your reference We require a print ready PDF and the Raw art files at the end of the project

Target Market(s)

See brief document and website

Industry/Entity Type

Real Estate Development

Font styles to use
Other font styles liked:
• MONTSERRAT REGULAR

Colors
0692cd
1b1b1b
aaaaaa

Requirements
Must have
• Bolderan Yards Tuggerah logo, disclaimer, as per brief,

```html
<!DOCTYPE html>
<html lang="en">
<head>
<meta charset="utf-8">
<title>Bolderan Yards Tuggerah – Flyer</title>
<link href="https://fonts.googleapis.com/css2?family=Oswald:wght@600;700&family=Lato:wght@400;700&display=swap" rel="stylesheet">
<style>
  :root {
    --stage: #3a393b;
    --teal: #1c93a8;
    --ink: #1b1b1b;
    --paper: #ffffff;
    --mist: #e4e4e4;
    --grey: #aaaaaa;
  }
  * { box-sizing: border-box; margin: 0; padding: 0; }
  html, body { width: 1200px; height: 1200px; overflow: hidden; }
  body { background: var(--stage); font-family: "Lato", sans-serif; color: var(--ink); position: relative; }

  .page { position: absolute; top: 354px; width: 440px; height: 564px; overflow: hidden; background: var(--paper); box-shadow: 0 10px 30px rgba(0,0,0,.45); }
  .page--front { left: 129px; }
  .page--back { left: 630px; }
  .page__art { position: absolute; inset: 0; width: 100%; height: 100%; }
  .abs { position: absolute; }

  /* front */
  .headline { left: 0; width: 100%; top: 358px; text-align: center; font-family: "Oswald", sans-serif; font-weight: 700; font-size: 24px; letter-spacing: -.2px; color: var(--ink); }
  .intro { left: 14px; width: 414px; font-size: 7.8px; line-height: 1.3; color: #222; }
  .brand { display: flex; align-items: center; gap: 6px; font-family: "Lato", sans-serif; font-weight: 700; color: var(--ink); }
  .brand__mark { width: 22px; height: 22px; border: 2px solid var(--teal); flex: none; }
  .brand__name { line-height: 1.15; letter-spacing: .6px; text-transform: uppercase; }
  .front-brand { left: 20px; top: 486px; font-size: 9px; width: 160px; }
  .contact-title { left: 250px; top: 483px; color: #fff; font-size: 16.5px; font-weight: 700; }
  .contact-line { display: flex; align-items: center; gap: 10px; color: #fff; }
  .front-phone { left: 227px; top: 508px; font-size: 16.5px; }
  .front-web { left: 227px; top: 534px; font-size: 10px; }
  .icon { flex: none; }

  /* back */
  .features-title { left: 37px; top: 161px; font-size: 18px; font-weight: 700; color: var(--teal); }
  .ticks { list-style: none; left: 36px; }
  .ticks li { display: flex; align-items: center; gap: 8px; font-size: 9.8px; height: 16.8px; color: #111; }
  .ticks--top { top: 185px; }
  .ticks--bottom { top: 405px; }
  .disclaimer { left: 14px; top: 458px; width: 416px; font-size: 6.1px; line-height: 1.33; color: #222; }
  .back-brand { left: 18px; top: 517px; font-size: 6.8px; width: 100px; color: #fff; }
  .back-brand .brand__mark { width: 18px; height: 18px; }
  .back-phone { left: 112px; top: 513px; font-size: 9.6px; gap: 8px; }
  .back-web { left: 112px; top: 530px; font-size: 6.5px; gap: 8px; }
  .partner { left: 282px; top: 520px; display: flex; align-items: center; gap: 6px; font-size: 10px; font-weight: 700; color: var(--ink); }
  .partner__mark { width: 11px; height: 11px; background: var(--teal); }
</style>
</head>
<body>

<!-- Front page -->
<section class="page page--front">
  <svg class="page__art" viewBox="0 0 550 705" preserveAspectRatio="none" aria-hidden="false">
    <defs>
      <linearGradient id="warehouseTone" x1="0" y1="0" x2="1" y2="1">
        <stop offset="0" stop-color="#5a5f66"/>
        <stop offset=".45" stop-color="#b48a5c"/>
        <stop offset="1" stop-color="#c9cfd6"/>
      </linearGradient>
      <linearGradient id="bodyTone" x1="0" y1="0" x2="1" y2="0">
        <stop offset="0" stop-color="#f2f2f2"/>
        <stop offset="1" stop-color="#d8d8d8"/>
      </linearGradient>
      <radialGradient id="portraitTone" cx=".5" cy=".45" r=".6">
        <stop offset="0" stop-color="#9aa3ad"/>
        <stop offset="1" stop-color="#3f4a58"/>
      </radialGradient>
    </defs>
    <rect x="0" y="0" width="550" height="440" fill="url(#warehouseTone)" role="img" aria-label="Cluttered warehouse with overflowing boxes on shelving"/>
    <path d="M0,355 C90,390 200,405 300,385 C400,365 470,340 550,330 L550,705 L0,705 Z" fill="var(--ink)"/>
    <path d="M0,385 C70,420 170,430 290,405 C400,382 480,370 550,380 L550,705 L0,705 Z" fill="var(--teal)"/>
    <path d="M0,420 C90,445 180,445 290,420 C390,398 470,400 550,455 L550,705 L0,705 Z" fill="url(#bodyTone)"/>
    <circle cx="289" cy="372" r="72" fill="url(#portraitTone)" stroke="var(--teal)" stroke-width="4" role="img" aria-label="Portrait of a stressed business owner on the phone"/>
    <path d="M0,705 L0,658 L220,658 C245,658 255,640 268,618 C278,600 285,597 300,597 L550,597 L550,705 Z" fill="var(--ink)"/>
  </svg>

  <h1 class="abs headline">Secure Your Businesses Future</h1>
  <p class="abs intro" style="top:402px">Bolderan Yards Micro-Commercial and Industrial Warehouse units are the most reliable way to get long term capital growth AND high yields on your investment - without the risk of the number one killer - vacancy.</p>
  <p class="abs intro" style="top:432px">Your investment is all about the numbers. Don't rely just on capital growth when you can access a heavily cashflow positive investment as well.</p>
  <p class="abs intro" style="top:461px">With Bolderan Yards you build your wealth faster and safer than the competition.</p>

  <div class="abs brand front-brand">
    <span class="brand__mark"></span>
    <span class="brand__name">Bolderan Yards Tuggerah</span>
  </div>

  <div class="abs contact-title">Contact Us</div>
  <div class="abs contact-line front-phone">
    <svg class="icon" width="12" height="16" viewBox="0 0 12 16"><path d="M3,1 L5,1 L6,5 L4,6 C4.5,8.5 6,10.5 8,11.5 L9.5,10 L12,12 L11,15 C5,15 1,9 2,2 Z" fill="var(--teal)"/></svg>
    <span>0400 555 018</span>
  </div>
  <div class="abs contact-line front-web">
    <svg class="icon" width="12" height="12" viewBox="0 0 12 12"><circle cx="6" cy="6" r="5.2" fill="none" stroke="var(--teal)" stroke-width="1.2"/><ellipse cx="6" cy="6" rx="2.2" ry="5.2" fill="none" stroke="var(--teal)" stroke-width="1"/><path d="M1,6 H11 M2,3.5 H10 M2,8.5 H10" stroke="var(--teal)" stroke-width="1"/></svg>
    <span>www.bolderanyardstuggerah.com.au</span>
  </div>
</section>

<!-- Back page -->
<section class="page page--back">
  <svg class="page__art" viewBox="0 0 550 705" preserveAspectRatio="none">
    <defs>
      <linearGradient id="officeTone" x1="0" y1="0" x2="1" y2="0">
        <stop offset="0" stop-color="#cfd0cf"/>
        <stop offset=".5" stop-color="#8b8a86"/>
        <stop offset="1" stop-color="#d8d8d6"/>
      </linearGradient>
      <linearGradient id="buildingTone" x1="0" y1="0" x2="0" y2="1">
        <stop offset="0" stop-color="#b9c8d6"/>
        <stop offset=".55" stop-color="#7c828a"/>
        <stop offset="1" stop-color="#9a9c9e"/>
      </linearGradient>
    </defs>
    <rect x="0" y="0" width="550" height="170" fill="url(#officeTone)" role="img" aria-label="Mezzanine office fit-out inside a warehouse unit"/>
    <path d="M0,110 C80,92 170,108 260,132 C380,164 470,150 550,95 L550,705 L0,705 Z" fill="var(--teal)"/>
    <path d="M0,150 C70,120 160,125 260,150 C380,180 470,175 550,155 L550,705 L0,705 Z" fill="var(--ink)"/>
    <path d="M0,225 C30,175 100,160 190,162 C310,166 400,210 550,188 L550,705 L0,705 Z" fill="var(--paper)"/>
    <rect x="0" y="348" width="550" height="155" fill="var(--teal)"/>
    <rect x="8" y="356" width="172" height="141" fill="url(#buildingTone)" role="img" aria-label="Render of unit frontages with roller doors"/>
    <rect x="188" y="356" width="172" height="141" fill="url(#buildingTone)" role="img" aria-label="Render of the estate entry building and driveway"/>
    <rect x="368" y="356" width="173" height="141" fill="url(#buildingTone)" role="img" aria-label="Render of the estate street frontage"/>
    <path d="M0,705 L0,632 L280,632 C300,632 308,650 318,668 C326,684 334,690 350,690 L550,690 L550,705 Z" fill="var(--ink)"/>
  </svg>

  <h2 class="abs features-title">Features</h2>
  <ul class="abs ticks ticks--top">
    <li><svg width="8" height="10" viewBox="0 0 8 10"><path d="M1,1 L6,5 L1,9" fill="none" stroke="var(--teal)" stroke-width="2.4"/></svg>Ideal for tradies, business space or personal storage</li>
    <li><svg width="8" height="10" viewBox="0 0 8 10"><path d="M1,1 L6,5 L1,9" fill="none" stroke="var(--teal)" stroke-width="2.4"/></svg>Superior heavy duty tilt-up concrete construction</li>
    <li><svg width="8" height="10" viewBox="0 0 8 10"><path d="M1,1 L6,5 L1,9" fill="none" stroke="var(--teal)" stroke-width="2.4"/></svg>Sizes from 30m² to 93m²</li>
    <li><svg width="8" height="10" viewBox="0 0 8 10"><path d="M1,1 L6,5 L1,9" fill="none" stroke="var(--teal)" stroke-width="2.4"/></svg>High clearance + office/ storage mezzanine's</li>
    <li><svg width="8" height="10" viewBox="0 0 8 10"><path d="M1,1 L6,5 L1,9" fill="none" stroke="var(--teal)" stroke-width="2.4"/></svg>24/7 video surveillance</li>
  </ul>
  <ul class="abs ticks ticks--bottom">
    <li><svg width="8" height="10" viewBox="0 0 8 10"><path d="M1,1 L6,5 L1,9" fill="none" stroke="var(--teal)" stroke-width="2.4"/></svg>Lights, power &amp; data in all units</li>
    <li><svg width="8" height="10" viewBox="0 0 8 10"><path d="M1,1 L6,5 L1,9" fill="none" stroke="var(--teal)" stroke-width="2.4"/></svg>Asset that will grow in value</li>
    <li><svg width="8" height="10" viewBox="0 0 8 10"><path d="M1,1 L6,5 L1,9" fill="none" stroke="var(--teal)" stroke-width="2.4"/></svg>Priced from $92,239 +GST</li>
  </ul>
  <p class="abs disclaimer">Disclaimer - The vendor, its sales agent and its representatives have made every effort to ensure the accuracy of information, however, they do not guarantee, warrant or represent that the information contained in this advertising and marketing material is correct. Any interested parties should make their own enquiries as to the accuracy of the information. We exclude all inferred or implied terms, conditions and warranties arising out of this document and any liability for loss or damage arising there from. All images are for illustration purposes only. Terms and conditions apply, contact agent for full details.</p>

  <div class="abs brand back-brand">
    <span class="brand__mark"></span>
    <span class="brand__name">Bolderan Yards Tuggerah</span>
  </div>
  <div class="abs contact-line back-phone">
    <svg class="icon" width="9" height="12" viewBox="0 0 12 16"><path d="M3,1 L5,1 L6,5 L4,6 C4.5,8.5 6,10.5 8,11.5 L9.5,10 L12,12 L11,15 C5,15 1,9 2,2 Z" fill="var(--teal)"/></svg>
    <span>0400 555 018</span>
  </div>
  <div class="abs contact-line back-web">
    <svg class="icon" width="9" height="9" viewBox="0 0 12 12"><circle cx="6" cy="6" r="5.2" fill="none" stroke="var(--teal)" stroke-width="1.2"/><ellipse cx="6" cy="6" rx="2.2" ry="5.2" fill="none" stroke="var(--teal)" stroke-width="1"/><path d="M1,6 H11" stroke="var(--teal)" stroke-width="1"/></svg>
    <span>www.bolderanyardstuggerah.com.au</span>
  </div>
  <div class="abs partner">
    <span class="partner__mark"></span>
    <span>Harlow Commercial</span>
  </div>
</section>

</body>
</html>
```